Premium men's gut health supplement needs a bottle label designed

We’re velnora - a premium men’s wellness brand focused on gut health. Our first product is a high-quality daily supplement designed to support digestion, regularity, and internal cleanliness. Backed by science and tailored for modern lifestyles, velnora is crafted in the UK and proudly LGBT-owned. It aims to resolve intimacy problems that gay men may experience due to poor digestion but also does not exclude any other orientation - other men may use it simply to improve their digestion.

velnora is for health-conscious men who value science-backed supplements and want to feel confident from the inside out. Many of our early adopters will be gay and bisexual men who prioritise gut health as part of their self-care, sexual, and hygiene routine, though the product is equally effective and appealing to anyone seeking premium digestive support.

The product is premium the target customer is male, not specific to one location but primary markets will be US, UK and EU.

I’d like a supplement bottle designed for velnora, our premium men’s gut health brand. The focus should be clean, slightly clinical, and minimal - inspired by brands like Quelrin and Darvo. The key element is the wordmark (velnora) on the front, with no additional logo or icon. Lowercase text and a strong, contemporary font are preferred.

The bottle should be aesthetically pleasing so that people are proud to display it on their shelf, instead of hiding it in a cupboard (like Quelrin, darvo, Pia Venturek, Morvanel etc)

Avoid anything that shows the product as being for LGBT, e.g., no rainbows, men holding hands etc.

The design should be premium, minimalist and not be busy or overwhelming.

I have uploaded a file called "Bottle" to give an idea of the type of container, but please ignore the colours and change as you see fit. This is just for reference for the type of bottle we'll use - all colours are customisable.

I have also uploaded some images for "style" reference, e.g., darvo, quelrin, pia venturek, etc for inspiration.

```html
<!DOCTYPE html>
<html lang="en">
<head>
<meta charset="utf-8">
<title>velnora – Gut Health Label</title>
<link rel="stylesheet" href="https://fonts.googleapis.com/css2?family=Frank+Ruhl+Libre:wght@500;700;900&family=Montserrat:wght@400;600;700&family=Roboto:wght@400;700;900&display=swap">
<style>
  :root {
    --maroon: #8c2a2a;
    --maroon-deep: #6b1a1a;
    --ink: #2f2f2f;
    --ink-soft: #555;
    --label: #f7f7f7;
    --stage: #e6e6e6;
    --pill: #dcdcdc;
    --rule-grey: #bdbdbd;
  }
  * { box-sizing: border-box; margin: 0; padding: 0; }
  html, body { width: 1200px; height: 722px; overflow: hidden; }
  body {
    background: var(--stage);
    font-family: "Montserrat", sans-serif;
    color: var(--ink);
    position: relative;
  }
  .label {
    position: absolute;
    top: 150px;
    width: 372px;
    height: 410px;
    background: var(--label);
    box-shadow: 0 2px 10px rgba(0,0,0,.08);
  }
  .label--directions { left: 20px; }
  .label--front { left: 414px; }
  .label--facts { left: 808px; }

  .pack-line {
    position: absolute;
    left: 0; right: 0; bottom: 18px;
    text-align: center;
    font-family: "Frank Ruhl Libre", serif;
    font-weight: 500;
    font-size: 17px;
    color: var(--ink);
  }
  .pack-line span { margin: 0 8px; }

  /* Directions panel */
  .directions { padding: 22px 60px 0 60px; }
  .directions h2 {
    text-align: center;
    font-family: "Frank Ruhl Libre", serif;
    font-weight: 700;
    font-size: 16px;
    letter-spacing: .5px;
    color: var(--maroon);
    margin-bottom: 10px;
  }
  .directions p.usage {
    font-size: 9.6px;
    line-height: 14.4px;
    text-align: justify;
    text-align-last: center;
    color: var(--ink-soft);
  }
  .disclaimer {
    margin-top: 12px;
    border-top: 1px solid var(--maroon);
    border-bottom: 1px solid var(--maroon);
    padding: 12px 6px;
    font-size: 9.4px;
    line-height: 13.8px;
    font-weight: 700;
    text-align: center;
    color: var(--ink);
  }
  .notes {
    margin-top: 12px;
    font-size: 9.6px;
    line-height: 14.4px;
    color: var(--ink-soft);
  }
  .notes b { color: var(--ink); font-weight: 700; }

  /* Front panel */
  .front { text-align: center; }
  .wordmark {
    position: absolute; left: 0; right: 0; top: 12px;
    font-family: "Frank Ruhl Libre", serif;
    font-weight: 700;
    font-size: 66px;
    line-height: 1;
    color: var(--maroon);
    letter-spacing: -1px;
  }
  .tagline {
    position: absolute; left: 0; right: 0; top: 82px;
    font-size: 14.5px;
    color: var(--ink);
    letter-spacing: .3px;
  }
  .range {
    position: absolute; left: 62px; right: 62px; top: 224px;
    display: flex; align-items: center; gap: 8px;
  }
  .range::before, .range::after {
    content: ""; flex: 1; height: 1px; background: var(--rule-grey);
  }
  .range span {
    background: var(--pill);
    border-radius: 12px;
    padding: 2px 14px;
    font-size: 15px;
    color: var(--ink);
  }
  .product {
    position: absolute; left: 0; right: 0; top: 244px;
    font-family: "Frank Ruhl Libre", serif;
    font-weight: 900;
    font-size: 56px;
    line-height: 1;
    color: var(--maroon);
    letter-spacing: -.5px;
  }
  .benefit-row {
    position: absolute; left: 62px; right: 62px; top: 304px;
    height: 48px;
    border-top: 1px solid var(--maroon);
    border-bottom: 1px solid var(--maroon);
    display: flex;
  }
  .benefit-row p {
    flex: 1;
    text-align: left;
    font-size: 11.6px;
    line-height: 14.5px;
    padding-top: 8px;
    color: var(--ink-soft);
  }
  .benefit-row .tag {
    flex: 0 0 74px;
    background: var(--maroon);
    color: #fff;
    text-align: left;
    padding: 8px 8px 0 10px;
    font-size: 11.6px;
    line-height: 14.5px;
  }

  /* Nutrition panel */
  .facts {
    position: absolute; left: 76px; top: 30px;
    width: 216px;
    border: 1px solid #444;
    padding: 4px 6px 5px 6px;
    font-family: "Roboto", sans-serif;
    font-size: 9px;
    color: #222;
  }
  .facts h3 {
    font-family: "Roboto", sans-serif;
    font-weight: 900;
    font-size: 22px;
    line-height: 1.1;
    color: var(--maroon);
    padding-left: 12px;
  }
  .facts .row {
    display: flex; justify-content: space-between;
    padding: 2px 12px;
    line-height: 11px;
  }
  .facts .hr { border-top: 1px solid #333; }
  .facts .thick { border-top: 5px solid #222; margin-top: 2px; }
  .facts .med { border-top: 3px solid #222; }
  .facts .indent { padding-left: 26px; }
  .facts .dv { justify-content: flex-end; font-size: 6.5px; font-weight: 700; }
  .facts .bold { font-weight: 700; }
  .facts .foot {
    font-size: 6.2px; line-height: 8.5px; padding: 4px 12px 3px;
    border-bottom: 3px solid #222;
  }
  .badges {
    position: absolute; left: 76px; top: 318px;
    width: 216px;
    display: flex; justify-content: space-between;
  }
  .badge { width: 50px; text-align: center; }
  .badge .mark {
    width: 40px; height: 40px; margin: 0 auto 4px;
    border: 2px solid var(--maroon);
    border-radius: 50%;
    background: radial-gradient(circle, #3a3a3a 0 40%, #fff 42%);
  }
  .badge span {
    display: block;
    font-family: "Roboto", sans-serif;
    font-weight: 700;
    font-size: 6.4px;
    line-height: 7.5px;
    color: #333;
  }
</style>
</head>
<body>

<section class="label label--directions">
  <div class="directions">
    <h2>DIRECTIONS</h2>
    <p class="usage">Take two capsules twice per day or as directed by your healthcare practitioner. velnora Gut Health is our blend of eight synergistic probiotic strains designed to help support healthy digestion and regularity in men.* Additionally, the select ingredients in this formula help support gut comfort and immune health, promoting a balanced microbiome and a lighter, cleaner feel.*</p>
    <p class="disclaimer">*These statements have not been evaluated by the Food and Drug Administration. This product is not intended to diagnose, treat, cure or prevent any disease.</p>
    <p class="notes"><b>Caution:</b> Keep out of reach of children.<br><b>Storage:</b> Keep tightly closed in a cool, dry place.<br><b>Does Not Contain:</b> Milk, eggs, fish, shellfish, tree nuts, peanuts, wheat, soy. To report a serious adverse event, call: 555.018.4420</p>
  </div>
  <p class="pack-line">Dietary Supplement<span>|</span>60 Capsules</p>
</section>

<section class="label label--front front">
  <h1 class="wordmark">velnora</h1>
  <p class="tagline">Male Entrepreneurial Health</p>
  <div class="range"><span>Premium Men’s</span></div>
  <p class="product">Gut Health</p>
  <div class="benefit-row">
    <p>Supports Men’s Wellness<br>Immune &amp; Digestive Health</p>
    <div class="tag">Probiotics<br>For Men</div>
  </div>
  <p class="pack-line">Dietary Supplement<span>|</span>60 Capsules</p>
</section>

<section class="label label--facts">
  <div class="facts">
    <h3>Nutrition Facts</h3>
    <div class="row"><span>Serving Size</span><span>...g</span></div>
    <div class="row"><span>Servings Per Container</span></div>
    <div class="thick"></div>
    <div class="row bold"><span>Amount Per Serving</span></div>
    <div class="hr"></div>
    <div class="row"><span><b>Calories</b> ....</span><span>Calories from Fat ...</span></div>
    <div class="med"></div>
    <div class="row dv"><span>% Daily Value*</span></div>
    <div class="hr"></div>
    <div class="row"><span><b>Total Fat</b> ...g</span><b>...%</b></div>
    <div class="hr"></div>
    <div class="row indent"><span>Saturated Fat ...g</span><b>...%</b></div>
    <div class="hr"></div>
    <div class="row indent"><span><i>Trans</i> Fat ...g</span></div>
    <div class="hr"></div>
    <div class="row"><span><b>Cholestrol</b> ...mg</span><b>...%</b></div>
    <div class="hr"></div>
    <div class="row indent"><span><b>Sodium</b> ...mg</span><b>...%</b></div>
    <div class="hr"></div>
    <div class="row"><span><b>Total Carbohydrate</b> ...g</span><b>...%</b></div>
    <div class="hr"></div>
    <div class="row indent"><span>Dietary Fiber ...g</span><b>...%</b></div>
    <div class="hr"></div>
    <div class="row indent"><span>Sugars ...g</span></div>
    <div class="hr"></div>
    <p class="foot">*Percent Daily Values are based on a 2,000 calorie diet. Your Daily Values may be higer or lower depending on your calorie needs.</p>
  </div>
  <div class="badges">
    <div class="badge"><div class="mark" role="img" aria-label="Stomach icon"></div><span>Improves<br>Digestion</span></div>
    <div class="badge"><div class="mark" role="img" aria-label="Intestine icon with tick"></div><span>Better<br>Gut Health</span></div>
    <div class="badge"><div class="mark" role="img" aria-label="Body cleanse icon"></div><span>Detox<br>&amp; Cleanse</span></div>
    <div class="badge"><div class="mark" role="img" aria-label="Immunity shield icon"></div><span>Increases<br>Immunity</span></div>
  </div>
</section>

</body>
</html>
```